Etiketten für Herstellung und Vertrieb von natürlichen Nahrungsergänzungsmitteln
Zielgruppe
Firma: veRivalo, siehe auch www.verivalo.de
Herstellung und Vertrieb von natürlichen Nahrungsergänzungsmitteln
Zielgruppe: 18+ Jahre in Deutschland, wird aber hauptsächlich von Frauen >40 Jahre gekauft
Aufgabenstellung
Das ist ein sehr interessantes Projekt. Wenn uns das Design gefällt, werden wir auch die weiteren Etiketten vom gleichen Designer neu designen lassen.
Um es dem Designer einfach zu machen und um möglichst viele Designer zu ermutigen mitzumachen, muss der Designer zunächst nur die Front des Etiketts designen. Nur der Gewinner muss dann am Ende das gesamte Etikett mit den weiteren Texten fertigstellen.
Das Design sollte hochwertig und im Stil wie bei kraftbeet sein (siehe z.B. https://www.kraftbeet.de/power-proteine).
Das Design sollte ansprechend, frisch und modern wirken. Die Frontseite sollte folgende Elemente enthalten:
a) Logo (kann in der Farbe geändert werden, wenn es besser zum Design passt)
b) Bilder der 3 Zutatengruppen Obst (40%), Gemüse (40%)und Kernen/Samen (20%) besteht. Wir könnten uns z.B. gut vorstellen, dass man ein paar Obstsorten, ein paar Gemüsesorten und ein paar Kerne/Samen in 3 Gruppen anordnet. Folgende Zutaten sind im Vital-Schub, natürlich müssen nicht alle dargestellt werden, sonst wäre es wahrscheinlich zu überlaufen:
Gemüse: Lauch, Rote Paprika, Karotte, Rettich, Maca, Brunnenkresse, Rote Beete, Petersilie, Grünkohl, Löwenzahnblätter, Brokkoli, Blumenkohl, Spinat, Artischocke, Fenchel, Mangold, Curcuma Extrakt, Traubenkernextrakt
Obst: Mango, Kiwi, Heidelbeere, Schwarze Johannisbeere, Erdbeere, Brombeere, Aronia, Acerola, Hagebutte, Cranberry, Gojibeeren
Kerne/Samen: Kürbiskerne, Leinsamen
c) Name des Produkts: Vital-Schub
d) Spruch: „Deine tägliche Vitamin-, Mineralstoff- und Omega-3-Quelle“
Stanzvorlage und Logo sind angehängt. Die Frontseite des Etiketts sollte auf der Mitte der Stanzvorlage sein. Links und rechts muss noch Platz für Text wie Zutaten und Nährstofftabelle bleiben.

```html
<!DOCTYPE html>
<html lang="de">
<head>
<meta charset="utf-8">
<title>veRivalo – Vital-Schub Etikett</title>
<link rel="stylesheet" href="https://fonts.googleapis.com/css2?family=Josefin+Sans:wght@300;400;600&display=swap">
<style>
  :root {
    --backdrop: #e7e4df;
    --kraft: #c39674;
    --kraft-light: #cda180;
    --kraft-dark: #b58766;
    --ink-white: #fbf7f2;
    --sepia: #7f6353;
    --sepia-dark: #5f483c;
  }
  * { margin: 0; padding: 0; box-sizing: border-box; }
  html, body { width: 1200px; height: 960px; overflow: hidden; }
  body {
    background: var(--backdrop);
    font-family: "Josefin Sans", sans-serif;
    position: relative;
  }
  .label-front {
    position: absolute;
    left: 330px;
    top: 30px;
    width: 540px;
    height: 900px;
    background: linear-gradient(90deg, var(--kraft-dark) 0%, var(--kraft-light) 35%, var(--kraft) 70%, var(--kraft-dark) 100%);
    overflow: hidden;
    color: var(--ink-white);
  }
  .ingredient-art {
    position: absolute;
    inset: 0;
    width: 540px;
    height: 900px;
  }
  .ingredient-art .item { fill: url(#ingredient-tone); }
  .ingredient-art .item-dark { fill: url(#ingredient-tone-dark); }
  .brand {
    position: absolute;
    top: 124px;
    left: 0;
    width: 100%;
    display: flex;
    justify-content: center;
    align-items: center;
    gap: 8px;
  }
  .brand-dot {
    width: 10px;
    height: 10px;
    border-radius: 50%;
    background: var(--ink-white);
  }
  .brand-name {
    font-size: 27px;
    font-weight: 600;
    letter-spacing: -0.5px;
    color: var(--ink-white);
  }
  .title-rule {
    position: absolute;
    left: 78px;
    width: 378px;
    height: 4px;
    background: var(--ink-white);
  }
  .title-rule.top { top: 481px; }
  .title-rule.bottom { top: 643px; }
  .product-name {
    position: absolute;
    top: 504px;
    left: 0;
    width: 100%;
    text-align: center;
    font-weight: 300;
    font-size: 64px;
    line-height: 66px;
    letter-spacing: 16px;
    text-transform: uppercase;
    padding-left: 16px;
  }
  .claim {
    position: absolute;
    top: 694px;
    left: 0;
    width: 100%;
    text-align: center;
    font-weight: 400;
    font-size: 19px;
    line-height: 28px;
    letter-spacing: 1.6px;
    text-transform: uppercase;
  }
</style>
</head>
<body>
  <main class="label-front">
    <svg class="ingredient-art" viewBox="0 0 540 900">
      <defs>
        <radialGradient id="ingredient-tone">
          <stop offset="0%" stop-color="#8d7262" stop-opacity="0.85"/>
          <stop offset="65%" stop-color="#7f6353" stop-opacity="0.55"/>
          <stop offset="100%" stop-color="#7f6353" stop-opacity="0"/>
        </radialGradient>
        <radialGradient id="ingredient-tone-dark">
          <stop offset="0%" stop-color="#5f483c" stop-opacity="0.8"/>
          <stop offset="65%" stop-color="#5f483c" stop-opacity="0.5"/>
          <stop offset="100%" stop-color="#5f483c" stop-opacity="0"/>
        </radialGradient>
      </defs>
      <ellipse class="item" cx="42" cy="193" rx="20" ry="26" role="img" aria-label="Brombeere"/>
      <ellipse class="item" cx="490" cy="193" rx="50" ry="64" role="img" aria-label="Brokkoliröschen"/>
      <ellipse class="item" cx="127" cy="288" rx="16" ry="32" transform="rotate(-35 127 288)" role="img" aria-label="Kürbiskern"/>
      <ellipse class="item" cx="324" cy="355" rx="58" ry="72" role="img" aria-label="Rettich mit Stiel"/>
      <ellipse class="item" cx="160" cy="396" rx="30" ry="38" role="img" aria-label="Erdbeere"/>
      <ellipse class="item" cx="23" cy="387" rx="42" ry="66" role="img" aria-label="Blumenkohl"/>
      <ellipse class="item" cx="479" cy="410" rx="22" ry="80" transform="rotate(20 479 410)" role="img" aria-label="Petersilienzweig"/>
      <ellipse class="item" cx="515" cy="540" rx="14" ry="18" role="img" aria-label="Brombeere"/>
      <ellipse class="item-dark" cx="19" cy="652" rx="36" ry="100" role="img" aria-label="Grünkohlblatt"/>
      <ellipse class="item" cx="17" cy="819" rx="12" ry="14" role="img" aria-label="Leinsamen"/>
      <ellipse class="item" cx="164" cy="805" rx="60" ry="58" role="img" aria-label="Blumenkohl"/>
      <ellipse class="item" cx="497" cy="751" rx="22" ry="130" transform="rotate(18 497 751)" role="img" aria-label="Karotte"/>
      <ellipse class="item" cx="394" cy="846" rx="14" ry="22" transform="rotate(40 394 846)" role="img" aria-label="Kürbiskern"/>
    </svg>

    <header class="brand">
      <span class="brand-dot"></span>
      <span class="brand-name">veRivalo</span>
    </header>

    <div class="title-rule top"></div>
    <h1 class="product-name">Vital<br>Schub</h1>
    <div class="title-rule bottom"></div>

    <p class="claim">Deine tägliche Vitamin-,<br>Mineralstoff- und Omega-3-Quelle</p>
  </main>
</body>
</html>
```